形状はチューブ式でです。やわらかく温かみがある、手作り感を重視したデザインを希望致します。シンプルでおしゃれなデザインでお願いします。
ボトル:たて90mm よこ109mm
印刷範囲:たて69mm よこ51.5mm

使用可能色は4色。
ベージュや茶系、ピンク等 暖色でやわらかい色
別紙に添付した画像の、fig&cocoaのロゴは使用してください。
ヘアパックは髪用です。今回はハンドクリームということで、ヘアパックとはデザインを変えていただきたいです。

添付したロゴの色は変えていただけます。
ご提案くださった皆様、大変申し訳ございません。
今回のハンドクリームは、FIG&COCOAシリーズがコンセプトでなく、【働く女姓】をコンセプトにしたほうがいいのではないかという声が社内で多かったため、
パッケージも全く新しいものを募集したく、内容を大幅に変更致します。

使用感等は変わらず、パッケージイメージのみ変えさせていただきます。

コンセプトは、働く女性の為のハンドクリーム。
スマホが使える、マウスがべたつかない、ペンが持てる…
オフィスで使用しやすいように、シンプルかつおしゃれなデザインを募集致します。

ベースの色は、白でお願い致します。
4色印刷で、何系の色使いでも結構です。

ご提案くださった皆様には、本当に申し訳ございませんが、
再度ご提案いただけましたら嬉しく思います。
度々申し訳ございません。
たまごとハチミツがメインではないものも
どなたかつくっていただけませんか?
よろしくお願い致します。

ご提案いただきまして、ありがとうございました。

シンプルかつおしゃれなデザインで、オフィスにぴったりだと思い、選定させていただきました。

46ものたくさんのご応募、誠にありがとうございました。
選びきれない素敵なデザインばかりでしたので
今後も、どうぞ宜しくお願い申し上げます。

```html
<!DOCTYPE html>
<html lang="en">
<head>
<meta charset="utf-8">
<title>fig&amp;cocoa hand cream label</title>
<link rel="stylesheet" href="https://fonts.googleapis.com/css2?family=Cormorant+Garamond:wght@400;500&display=swap">
<style>
  :root {
    --paper: #ffffff;
    --cocoa: #8a7560;
    --cocoa-soft: #a08d78;
    --ink: #4a3f35;
    --honey: #ecdcae;
  }
  html, body {
    margin: 0;
    padding: 0;
    width: 900px;
    height: 1200px;
    overflow: hidden;
    background: var(--paper);
  }
  .label {
    position: relative;
    width: 900px;
    height: 1200px;
    background: var(--paper);
    font-family: "Cormorant Garamond", Georgia, serif;
    color: var(--cocoa);
  }
  .frame-art {
    position: absolute;
    inset: 0;
  }
  .brand-name {
    position: absolute;
    top: 182px;
    left: 0;
    width: 100%;
    margin: 0;
    text-align: center;
    font-size: 40px;
    font-weight: 500;
    line-height: 1;
    letter-spacing: 1px;
    color: var(--cocoa);
  }
  .product-name {
    position: absolute;
    top: 240px;
    left: 0;
    width: 100%;
    margin: 0;
    text-align: center;
    font-size: 104px;
    font-weight: 400;
    line-height: 1;
    color: var(--cocoa);
  }
  .usage-icons {
    position: absolute;
    top: 410px;
    left: 0;
    width: 100%;
  }
  .concept {
    position: absolute;
    top: 640px;
    left: 238px;
    width: 500px;
    margin: 0;
    font-size: 23px;
    line-height: 1.2;
    color: var(--ink);
  }
  .hand-art {
    position: absolute;
    left: 270px;
    top: 765px;
    width: 465px;
    height: 290px;
    background: linear-gradient(160deg, var(--cocoa-soft), var(--cocoa));
    border-radius: 140px 40px 20px 20px;
  }
</style>
</head>
<body>
<main class="label">
  <svg class="frame-art" width="900" height="1200" viewBox="0 0 900 1200">
    <rect x="20" y="20" width="860" height="1160" fill="var(--honey)" role="img" aria-label="Floral ornament border pattern"/>
    <path class="frame-panel" fill="var(--paper)" stroke="var(--cocoa)" stroke-width="10"
      d="M135 75 H765 A60 60 0 0 0 825 135 V1065 A60 60 0 0 0 765 1125 H135 A60 60 0 0 0 75 1065 V135 A60 60 0 0 0 135 75 Z"/>
    <path class="frame-inner-line" fill="none" stroke="var(--cocoa)" stroke-width="3"
      d="M140 92 H760 A62 62 0 0 0 808 140 V1060 A62 62 0 0 0 760 1108 H140 A62 62 0 0 0 92 1060 V140 A62 62 0 0 0 140 92 Z"/>
  </svg>

  <p class="brand-name">fig&amp;cocoa</p>
  <h1 class="product-name">hand cream</h1>

  <svg class="usage-icons" width="900" height="190" viewBox="0 0 900 190">
    <g class="icon-phone" fill="none" stroke="var(--cocoa)" stroke-width="8">
      <rect x="225" y="20" width="110" height="150" rx="14"/>
      <rect x="242" y="36" width="76" height="76" rx="4" stroke-width="5"/>
      <circle cx="255" cy="140" r="8" stroke-width="5"/>
      <circle cx="280" cy="140" r="8" stroke-width="5"/>
      <circle cx="305" cy="140" r="8" stroke-width="5"/>
    </g>
    <g class="icon-pen" fill="none" stroke="var(--cocoa)" stroke-width="8" stroke-linejoin="round">
      <path d="M510 10 L528 28 L416 140 L392 158 L398 130 Z"/>
      <path d="M416 140 L398 130" stroke-width="5"/>
      <path d="M490 30 L508 48" stroke-width="5"/>
    </g>
    <g class="icon-mouse" fill="none" stroke="var(--cocoa)" stroke-width="8">
      <path d="M625 18 C610 8 640 0 630 14" stroke-width="4"/>
      <rect x="585" y="40" width="90" height="130" rx="45"/>
      <path d="M585 90 H675 M630 40 V90" stroke-width="5"/>
      <rect x="623" y="56" width="14" height="22" rx="7" stroke-width="4"/>
    </g>
  </svg>

  <p class="concept">The hand cream for the woman who works.<br>It can have a pen which can use a smart phone<br>and which is not sticky in a mouse.</p>

  <div class="hand-art" role="img" aria-label="Silhouette of a graceful open hand and forearm"></div>
</main>
</body>
</html>
```